"Maple Nook" needs a A5 flyer for its "Art Contest"

Maple Nook needs a double sided A5 Flyer that illustrates in a child-friendly look the following competition:

Search for the up and coming Bright Sprout. The aim of our Bright Sprout is to allow our children to explore the artist within them and motivate them to express their talents through the fine art of drawing and painting.

Description: I have an art school, "Maple Nook", where children of 3-5 years old attend and learn how to paint and draw. We are making a competition where each child gets to draw a picture which we will upload to Chirpwall and parents will vote for best picture. We need to distribute to the parents a flyer with following content.

Competition Name: Bright Sprout

Front Side (content):
No major text on the front. Only the Logo and messages grabbing the readers attention such as "Who will be our next Artist?", "Vote for your Child", "Like Us on our Chirpwall Page".

Back Side (content):
Back side content is divided into 3 sections:

Section1:
How it Works?
Every child of every class will participate. Photos will be grouped by class.
There will be a Bright Sprout for each class, and there will be a Bright Sprout for the school.

Section2:
How to Participate?
In our search for ‘Bright Sprout’, we will select one piece of artwork from each child in the school, photograph it and upload it to our Chirpwall page.
Vote for your favourite painting by following the steps below:
1- From your chirpwall account go to www.chirpwall.example/Maple Nook
and “Like Us” to become a fan
2- Click on the“Bright Sprout” from the application menu
3- Browse through the different classes and vote for each picture you like
4- Invite your friends to vote for the picture you like to increase the chances of winning
The artist of the painting with most “Likes” will be crowned ‘Bright Sprout’.

Section3:
Note (in the footer):
Please note that the winner’s photo will be displayed in our “Bright Sprout” Frame on our Chirpwall landing page. If you do not want your child’s photograph to be posted on our Chirpwall page in this manner, please let us know by sending an e-mail.
, Maple Nook needs a double sided A5 Flyer that illustrates in a child-friendly look the following competition:

Front Side (content):

Back Side (content):

Section1:
How it Works?

Section2:
How to Participate?

Section3:
Note (in the footer):

Reason: To give more time for improvements on submitted designs and if possible some additional submissions.

Target Market(s)

Parents of the children attending at our school, Parents of the children attending at our school

Industry/Entity Type

Painting

Requirements
Must have
• Colors used in the design should be strict to our logo colors. We have 4 colors in our logo feel free to use one or all of them through out the design:
#6CB53C
#DB2718
#5D9DD5
#F4D602

The elements in our logo are playful and hand drawn and written, so the flyer design should reflect the hand made style rather than solid elements and objects., Colors used in the design should be strict to our logo colors. We have 4 colors in our logo feel free to use one or all of them through out the design:
#6CB53C
#DB2718
#5D9DD5
#F4D602

The elements in our logo are playful and hand drawn and written, so the flyer design should reflect the hand made style rather than solid elements and objects.
Should not have
• Images of real children., Images of real children.

```html
<!DOCTYPE html>
<html lang="en">
<head>
<meta charset="utf-8">
<title>Maple Nook – Bright Sprout Flyer</title>
<link rel="stylesheet" href="https://fonts.googleapis.com/css2?family=Cabin+Sketch:wght@400;700&family=Amatic+SC:wght@400;700&display=swap">
<style>
  :root {
    --green: #6CB53C;
    --red: #DB2718;
    --blue: #5D9DD5;
    --yellow: #F4D602;
    --backdrop: #5B9BD3;
    --paper: #F3F3F1;
    --paper-shade: #E4E4E2;
    --fold: rgba(150,150,150,0.35);
  }
  html, body {
    margin: 0;
    padding: 0;
    width: 1200px;
    height: 1000px;
    overflow: hidden;
    background: var(--backdrop);
  }
  .canvas {
    position: relative;
    width: 1200px;
    height: 1000px;
  }
  .sheet {
    position: absolute;
    overflow: hidden;
  }
  .paper {
    background: linear-gradient(135deg, #F7F7F5 0%, var(--paper) 50%, var(--paper-shade) 100%);
  }
  .fold-lines {
    position: absolute;
    inset: 0;
    width: 100%;
    height: 100%;
    pointer-events: none;
  }

  /* Front side */
  .front {
    left: 60px;
    top: 125px;
    width: 522px;
    height: 747px;
  }
  .headline-word {
    position: absolute;
    margin: 0;
    font-family: "Cabin Sketch", cursive;
    font-weight: 700;
    font-variant: small-caps;
    font-size: 68px;
    line-height: 1;
    letter-spacing: 1px;
    white-space: nowrap;
  }
  .word-who { left: 55px; top: 85px; color: var(--green); }
  .word-be { left: 177px; top: 195px; color: var(--blue); }
  .word-next { left: 75px; top: 300px; color: var(--red); }
  .word-bright { left: 228px; top: 405px; color: var(--green); }
  .word-sprout { left: 75px; top: 505px; color: var(--blue); }

  .social-block {
    position: absolute;
    left: 32px;
    top: 679px;
    font-family: "Cabin Sketch", cursive;
    font-weight: 700;
    font-variant: small-caps;
  }
  .social-label {
    color: var(--green);
    font-size: 15px;
    margin: 0 0 6px 0;
  }
  .social-link {
    display: flex;
    align-items: center;
    gap: 8px;
    color: var(--blue);
    font-size: 15px;
  }
  .social-dot {
    width: 18px;
    height: 18px;
    border-radius: 50%;
    background: var(--blue);
    display: inline-block;
  }
  .school-name {
    position: absolute;
    left: 360px;
    top: 688px;
    display: flex;
    align-items: center;
    gap: 8px;
    font-family: "Cabin Sketch", cursive;
    font-weight: 700;
    font-size: 26px;
    color: var(--green);
  }
  .school-square {
    width: 22px;
    height: 22px;
    background: var(--green);
    display: inline-block;
  }

  /* Back side */
  .back {
    left: 610px;
    top: 127px;
    width: 522px;
    height: 746px;
    background: var(--yellow);
  }
  .back-paper {
    position: absolute;
    left: 18px;
    top: 20px;
    width: 480px;
    height: 700px;
    border-radius: 3px;
  }
  .stars {
    position: absolute;
    left: 378px;
    top: 40px;
    width: 76px;
    height: 40px;
    background: linear-gradient(90deg, var(--yellow), var(--blue) 60%, var(--green));
    opacity: 0.75;
    border-radius: 40%;
  }
  .section-title {
    position: absolute;
    margin: 0;
    font-family: "Cabin Sketch", cursive;
    font-weight: 700;
    font-size: 27px;
    color: var(--green);
    white-space: nowrap;
  }
  .title-works { left: 42px; top: 73px; }
  .title-participate { left: 42px; top: 172px; }
  .title-note { left: 42px; top: 490px; font-size: 21px; }

  .body-text {
    position: absolute;
    margin: 0;
    font-family: "Amatic SC", cursive;
    font-weight: 700;
    font-size: 14px;
    line-height: 18px;
    color: var(--blue);
    letter-spacing: 0.3px;
  }
  .text-works { left: 45px; top: 115px; width: 460px; }
  .text-note { left: 45px; top: 525px; width: 440px; }

  .steps {
    position: absolute;
    left: 62px;
    top: 222px;
    margin: 0;
    padding: 0;
    list-style: none;
    width: 420px;
  }
  .step {
    position: absolute;
    left: 0;
    display: flex;
    align-items: flex-start;
    gap: 16px;
  }
  .step-1 { top: 0; }
  .step-2 { top: 73px; }
  .step-3 { top: 136px; }
  .step-4 { top: 196px; }
  .step-marker {
    flex: none;
    width: 19px;
    height: 19px;
    font-family: "Cabin Sketch", cursive;
    font-weight: 700;
    font-size: 12px;
    line-height: 19px;
    text-align: center;
    color: var(--yellow);
  }
  .marker-circle { background: var(--blue); border-radius: 50%; }
  .marker-diamond { background: var(--red); transform: rotate(45deg); width: 16px; height: 16px; line-height: 16px; }
  .marker-diamond span { display: inline-block; transform: rotate(-45deg); }
  .marker-hex { background: var(--green); clip-path: polygon(25% 0, 75% 0, 100% 50%, 75% 100%, 25% 100%, 0 50%); }
  .marker-square { background: var(--blue); }
  .step-text {
    font-family: "Amatic SC", cursive;
    font-weight: 700;
    font-size: 14px;
    line-height: 17px;
    color: var(--blue);
    margin: 0;
  }

  .cta {
    position: absolute;
    left: 0;
    width: 522px;
    top: 620px;
    margin: 0;
    text-align: center;
    font-family: "Cabin Sketch", cursive;
    font-weight: 700;
    font-size: 42px;
    color: var(--green);
    letter-spacing: 2px;
  }

  .handprint {
    position: absolute;
    background: radial-gradient(ellipse at center, rgba(219,39,24,0.85) 0%, rgba(219,39,24,0.45) 45%, rgba(219,39,24,0) 72%);
  }
  .hand-left { left: 0; top: 640px; width: 115px; height: 106px; }
  .hand-right { left: 385px; top: 590px; width: 125px; height: 150px; }
</style>
</head>
<body>
<main class="canvas">

  <!-- Front side -->
  <section class="sheet front paper" aria-label="Flyer front">
    <svg class="fold-lines" viewBox="0 0 522 747" preserveAspectRatio="none" aria-hidden="true">
      <g stroke="var(--fold)" stroke-width="2">
        <line x1="0" y1="90" x2="522" y2="92"/>
        <line x1="0" y1="185" x2="522" y2="186"/>
        <line x1="0" y1="280" x2="522" y2="281"/>
        <line x1="0" y1="373" x2="522" y2="374"/>
        <line x1="0" y1="465" x2="522" y2="466"/>
        <line x1="0" y1="560" x2="522" y2="561"/>
        <line x1="0" y1="653" x2="522" y2="654"/>
      </g>
    </svg>

    <h1 class="headline" aria-label="Who will be our next Bright Sprout?">
      <span class="headline-word word-who">Who Will</span>
      <span class="headline-word word-be">Be Our</span>
      <span class="headline-word word-next">Next</span>
      <span class="headline-word word-bright">Bright</span>
      <span class="headline-word word-sprout">Sprout?</span>
    </h1>

    <div class="social-block">
      <p class="social-label">Like us on Chirpwall:</p>
      <div class="social-link"><span class="social-dot"></span>www.chirpwall.example/Maple Nook</div>
    </div>

    <div class="school-name"><span class="school-square"></span>Maple Nook</div>
  </section>

  <!-- Back side -->
  <section class="sheet back" aria-label="Flyer back">
    <div class="back-paper paper">
      <svg class="fold-lines" viewBox="0 0 480 700" preserveAspectRatio="none" aria-hidden="true">
        <g stroke="var(--fold)" stroke-width="2">
          <line x1="0" y1="73" x2="480" y2="74"/>
          <line x1="0" y1="168" x2="480" y2="169"/>
          <line x1="0" y1="262" x2="480" y2="263"/>
          <line x1="0" y1="355" x2="480" y2="356"/>
          <line x1="0" y1="448" x2="480" y2="449"/>
          <line x1="0" y1="543" x2="480" y2="544"/>
          <line x1="0" y1="636" x2="480" y2="637"/>
        </g>
      </svg>
    </div>

    <div class="stars" role="img" aria-label="Three small hand-drawn stars"></div>

    <h2 class="section-title title-works">How it works</h2>
    <p class="body-text text-works">Every child of every class will participate. Photos will be grouped by class.<br>There will be a Bright Sprout for each class, and there will be a Bright Sprout for the school.</p>

    <h2 class="section-title title-participate">How to participate</h2>
    <ol class="steps">
      <li class="step step-1">
        <span class="step-marker marker-circle">1</span>
        <p class="step-text">From your chirpwall account go to www.chirpwall.example/Maple Nook<br>and "Like Us" to become a fan</p>
      </li>
      <li class="step step-2">
        <span class="step-marker marker-diamond"><span>2</span></span>
        <p class="step-text">Click on the "Bright Sprout" from the application menu</p>
      </li>
      <li class="step step-3">
        <span class="step-marker marker-hex">3</span>
        <p class="step-text">Browse through the different classes and vote for each picture you like</p>
      </li>
      <li class="step step-4">
        <span class="step-marker marker-square">4</span>
        <p class="step-text">Invite your friends to vote for the picture you like to increase the chances<br>of winning. The artist of the painting with most "Likes"<br>will be crowned "Bright Sprout"</p>
      </li>
    </ol>

    <h2 class="section-title title-note">*Note</h2>
    <p class="body-text text-note">Please note that the winner's photo will be displayed in our "Bright Sprout" Frame on our Chirpwall landing page. If you do not want your child's photograph to be posted on our Chirpwall page in this manner, please let us know by sending an e-mail.</p>

    <p class="cta">JOIN NOW!</p>

    <div class="handprint hand-left" role="img" aria-label="Red painted child handprint"></div>
    <div class="handprint hand-right" role="img" aria-label="Red painted child handprint"></div>
  </section>

</main>
</body>
</html>
```